Fontaneau Bayou Grillhouse (Owners Card)

Need a classy, but modern business card. I have included a promotional card for the steakhouse. I need one for myself (the owner) that is more professional.

Target Market(s)

General Public

Industry/Entity Type

Food service

Contact Information for Business Card

Name, business address, phone number, email, logo

Font styles to use
Serif
Sans Serif
Decorative
Script

Requirements
Must have
• My name (Darvin Okafor), business address (627 Harlow Avenue), phone number (520) 394-2751, email (Dokaforzp4@mailbrook.net. On the back of the card: Psalms 27 1 The LORD is my light and my salvation— whom shall I fear? The LORD is the stronghold of my life— of whom shall I be afraid? 2 When the wicked advance against me to devour me, it is my enemies and my foes who will stumble and fall. 3 Though an army besiege me, my heart will not fear; though war break out against me, even then I will be confident.
Nice to have
• Something that’s bold, but modern and professional.

```html
<!DOCTYPE html>
<html lang="en">
<head>
<meta charset="utf-8">
<title>Fontaneau Bayou Grillhouse – Owner Card</title>
<link rel="stylesheet" href="https://fonts.googleapis.com/css2?family=Cinzel:wght@700&family=Roboto:wght@400;500&family=Montserrat:wght@400;600&display=swap">
<style>
  :root {
    --bg: #2b2b2b;
    --card-dark: #242424;
    --card-light: #ffffff;
    --ink: #1c1c1c;
    --ink-soft: #333333;
    --paper-text: #f4f4f4;
    --green: #7ab648;
    --orange: #e5992f;
    --red: #c1272d;
  }
  * { box-sizing: border-box; margin: 0; padding: 0; }
  html, body {
    width: 1200px; height: 985px; overflow: hidden;
    background: var(--bg);
  }
  .canvas {
    width: 1200px; height: 985px;
    display: flex; flex-direction: column; align-items: center; justify-content: center;
    gap: 44px;
  }
  .card {
    position: relative;
    width: 760px; height: 434px;
    border-radius: 22px;
    overflow: hidden;
    box-shadow: 0 14px 30px rgba(0,0,0,.45);
  }

  /* Back side */
  .card--back {
    background: var(--card-dark);
    color: var(--paper-text);
    font-family: "Montserrat", sans-serif;
    text-align: center;
    padding-top: 62px;
  }
  .brand-mark {
    font-family: "Cinzel", serif;
    font-weight: 700;
    color: var(--red);
    line-height: 1.05;
  }
  .card--back .brand-mark { font-size: 30px; margin-bottom: 22px; }
  .verse { font-size: 13.5px; line-height: 1.45; letter-spacing: .3px; }
  .verse-divider {
    width: 150px; height: 1px; margin: 9px auto;
    background: var(--paper-text); opacity: .8;
  }
  .card--back .web {
    margin-top: 20px; font-size: 17px; letter-spacing: .4px;
  }
  .web-accent { color: var(--orange); font-weight: 600; }

  /* Front side */
  .card--front {
    background: var(--card-light);
    color: var(--ink);
    font-family: "Roboto", sans-serif;
  }
  .owner {
    position: absolute; left: 56px; top: 112px;
  }
  .owner-name {
    font-family: "Cinzel", serif; font-weight: 700;
    font-size: 30px; letter-spacing: .5px;
    background: linear-gradient(90deg, var(--green), var(--orange) 55%, var(--red));
    -webkit-background-clip: text; background-clip: text; color: transparent;
  }
  .owner-title { font-size: 17px; color: var(--ink-soft); margin-top: -2px; }
  .rule {
    position: absolute; left: 50px; right: 44px; top: 196px;
    height: 2px; background: var(--ink);
  }
  .brand-block {
    position: absolute; right: 60px; top: 96px; width: 300px;
    text-align: center;
  }
  .card--front .brand-mark { font-size: 33px; }
  .contacts {
    position: absolute; left: 44px; top: 222px;
    list-style: none; font-size: 18px; color: var(--ink);
  }
  .contacts li { display: flex; align-items: center; gap: 14px; margin-bottom: 10px; }
  .contacts svg { width: 18px; height: 18px; flex: none; }
  .address {
    position: absolute; right: 60px; top: 226px;
    display: flex; align-items: center; gap: 14px;
    font-size: 19px; letter-spacing: .3px;
  }
  .address svg { width: 18px; height: 24px; }
  .band {
    position: absolute; left: 0; right: 0; bottom: 0; height: 22px;
    display: flex;
  }
  .band span { flex: 1; }
  .band .g { background: var(--green); }
  .band .o { background: var(--orange); }
  .band .r { background: var(--red); }
</style>
</head>
<body>
<main class="canvas">

  <section class="card card--back" aria-label="Card back">
    <p class="brand-mark">Fontaneau<br>Bayou Grillhouse</p>
    <p class="verse">The LORD is my light and my salvation—whom shall I fear?<br>The LORD is the stronghold of my life—of whom shall I be afraid?</p>
    <div class="verse-divider"></div>
    <p class="verse">When the wicked advance against me to devour me, it is my enemies and my foes<br>who will stumble and fall.</p>
    <div class="verse-divider"></div>
    <p class="verse">Though an army besiege me, my heart will not fear; though war break out against<br>me, even then I will be confident.</p>
    <p class="web">www.<span class="web-accent">fontbayou</span>.com</p>
  </section>

  <section class="card card--front" aria-label="Card front">
    <div class="owner">
      <h1 class="owner-name">DARVIN OKAFOR</h1>
      <p class="owner-title">Owner/CEO</p>
    </div>

    <div class="brand-block">
      <p class="brand-mark">Fontaneau<br>Bayou Grillhouse</p>
    </div>

    <div class="rule"></div>

    <ul class="contacts">
      <li>
        <svg viewBox="0 0 24 24" aria-hidden="true"><path fill="#7ab648" d="M6.6 10.8a15 15 0 0 0 6.6 6.6l2.2-2.2a1 1 0 0 1 1-.25 11.4 11.4 0 0 0 3.6.57 1 1 0 0 1 1 1V20a1 1 0 0 1-1 1A17 17 0 0 1 3 4a1 1 0 0 1 1-1h3.5a1 1 0 0 1 1 1c0 1.25.2 2.45.57 3.57a1 1 0 0 1-.25 1z"/></svg>
        (520) 394-2751
      </li>
      <li>
        <svg viewBox="0 0 24 24" aria-hidden="true"><rect x="2" y="5" width="20" height="14" rx="1.5" fill="#c1272d"/><path d="M2.5 6l9.5 7 9.5-7" fill="none" stroke="#fff" stroke-width="1.6"/></svg>
        Dokaforzp4@mailbrook.net
      </li>
      <li>
        <svg viewBox="0 0 24 24" aria-hidden="true"><g fill="none" stroke="#7ab648" stroke-width="1.8"><circle cx="12" cy="12" r="9.5"/><ellipse cx="12" cy="12" rx="4.2" ry="9.5"/><path d="M2.5 12h19M4 7h16M4 17h16"/></g></svg>
        www.fontbayou.com
      </li>
    </ul>

    <div class="address">
      <svg viewBox="0 0 18 24" aria-hidden="true"><path fill="#c1272d" d="M9 0a9 9 0 0 0-9 9c0 6.5 9 15 9 15s9-8.5 9-15a9 9 0 0 0-9-9zm0 12.5A3.5 3.5 0 1 1 9 5.5a3.5 3.5 0 0 1 0 7z"/></svg>
      627 Harlow Avenue
    </div>

    <div class="band" aria-hidden="true"><span class="g"></span><span class="o"></span><span class="r"></span></div>
  </section>

</main>
</body>
</html>
```